Design a great website for our amazing new country club in Southern California!

Our old neighborhood golf club is being transformed into a 100% new world-class club located down the street from the old location. We want a new website look that projects our new image. However because the club hasn't been built yet, we don't have a lot of images--just a new logo and a few renderings. So we will add images in the coming months as things get built. In the meantime, for things such as restaurant or swimming or tennis pics, feel free to plug in stock internet images for now. And regarding the movie file, we had an idea for a dramatic headline slowly rising over the clubhouse. It's just an idea, however, we're not married to it. We need to get creative here, as we have so few images. Oh, and we definitely want one main graphic on the home page. We don't like the slide-show effect--looks cheap. And finally, the landing page will be a 'public' page with other pages aimed at attracting new members. There will also be a 'Members area' that is password-protected. Site maps and rough copy for each of the two sections is included. Good luck!! :-) Please view our current website: sagemeadowcc.com

Wealthy folks who like golf, sports and dining. Our memberships range in price from $18,000 to $130,000.

Club

Coded - Design and coding required

5+ page

Sans Serif

• a GORGEOUS home page, with buttons and features that will remain static on all other pages. We want the navigation buttons along the top with pull-downs. Only the areas below the nav buttons will change. We want this site to look very clean and classy.
• Maybe have the button 'glow' or enlarge or whatever when you roll over them. Whatever can spruce up the simple classy design. Maybe so some special effect to the SM logo as well. As long as it looks classy, that's the main thing. And if you can find some good generic images of golf, dining, swimming, tennis, whatever on the net, feel free to use them.
• No slide show effects, with multiple images changing.

```html
<!DOCTYPE html>
<html lang="en">
<head>
<meta charset="utf-8">
<title>Sage Meadow Country Club</title>
<link href="https://fonts.googleapis.com/css2?family=Cinzel:wght@400;700&family=Roboto:wght@300;400;500&display=swap" rel="stylesheet">
<style>
:root{
  --green:#4a5a26;
  --green-dark:#3a4720;
  --green-deep:#2e3a1b;
  --gold:#c6b06a;
  --ink:#444;
  --muted:#666;
  --line:#d8d8d8;
  --white:#fff;
}
*{margin:0;padding:0;box-sizing:border-box}
html,body{width:1200px;height:3030px;overflow:hidden;background:var(--white)}
body{font-family:'Roboto',sans-serif;color:var(--ink);position:relative}

/* header */
.header{position:absolute;left:0;top:0;width:1200px;height:119px;background:var(--white);border-top:5px solid var(--gold)}
.social{position:absolute;display:flex;gap:12px}
.social span{width:40px;height:40px;border:2px solid #333;border-radius:50%;display:flex;align-items:center;justify-content:center;color:#333}
.social svg{width:18px;height:18px;fill:none;stroke:currentColor;stroke-width:2;stroke-linecap:round;stroke-linejoin:round}
.header .social{left:100px;top:36px}
.phone{position:absolute;left:752px;top:46px;font-size:17px;color:#333;display:flex;align-items:center;gap:8px}
.login{position:absolute;left:966px;top:32px;width:134px;height:48px;background:var(--gold);color:var(--white);font-size:16px;display:flex;align-items:center;justify-content:center}
.nav{position:absolute;left:0;top:119px;width:1200px;height:67px;background:var(--green);border-bottom:3px solid var(--green-dark)}
.nav a{position:absolute;top:22px;color:var(--white);font-size:16px;font-weight:500;text-decoration:none}

/* brand */
.brand{position:absolute;left:490px;top:-30px;width:220px;height:206px;border-radius:50%;background:var(--white);text-align:center;z-index:5}
.brand-mark{font-family:'Cinzel',serif;font-weight:700;color:#222;line-height:1}
.brand .mono{position:absolute;left:0;right:0;top:48px;font-size:54px}
.brand .name{position:absolute;left:0;right:0;top:117px;font-size:23px}
.brand .sub{position:absolute;left:0;right:0;top:146px;font-size:11px;letter-spacing:2px;font-weight:400}

/* hero */
.hero{position:absolute;left:0;top:186px;width:1200px;height:507px;background:linear-gradient(180deg,#8f9a86 0%,#7c8b6e 35%,#6b7b5c 60%,#8a7b66 100%)}
.hero-title{position:absolute;left:277px;top:127px;width:648px;height:101px;background:rgba(62,78,30,.92);color:var(--white);font-family:'Cinzel',serif;font-size:72px;text-align:center;line-height:101px}
.hero-text{position:absolute;left:250px;top:244px;width:700px;color:var(--white);font-size:16px;line-height:30px;text-align:center}
.hero-btn{position:absolute;left:525px;top:339px;width:150px;height:57px;border:2px solid var(--white);color:var(--white);font-size:17px;display:flex;align-items:center;justify-content:center}
.arrow{position:absolute}

/* section heading */
.heading{position:absolute;font-family:'Cinzel',serif;font-size:30px;color:var(--green-dark);display:flex;align-items:center;gap:12px;white-space:nowrap}
.heading i{display:block;width:24px;height:24px;background:currentColor}
.heading em{font-style:normal;color:var(--gold)}
.heading.center{left:0;width:1200px;justify-content:center}
.heading.light{color:var(--white)}

/* welcome */
.welcome-text{position:absolute;left:99px;top:812px;width:590px;font-size:13px;line-height:22px;color:#555}
.btn-dark{position:absolute;background:var(--green-dark);color:var(--white);font-size:15px;display:flex;align-items:center;justify-content:center}
.video{position:absolute;left:723px;top:747px;width:376px;height:275px;border:7px solid var(--white);box-shadow:0 10px 22px rgba(0,0,0,.3);background:linear-gradient(180deg,#6f95c7 0%,#a9c2de 40%,#8d8170 62%,#5e5448 100%)}
.play{position:absolute;left:157px;top:105px;width:50px;height:50px;border:2px solid var(--white);border-radius:50%;background:rgba(0,0,0,.35)}
.video-bar{position:absolute;left:0;right:0;bottom:0;height:22px;background:rgba(0,0,0,.55)}

/* guest info */
.guest{position:absolute;left:0;top:1062px;width:1200px;height:483px;background:linear-gradient(180deg,#4b5b2a,#3f4e22)}
.info{position:absolute;width:260px;text-align:center;color:var(--white)}
.info svg{display:block;margin:0 auto}
.info h3{margin-top:40px;font-size:19px;font-weight:500}
.info p{margin-top:10px;font-size:13px;line-height:22px;padding:0 40px}
.divider{position:absolute;top:1215px;width:1px;height:275px;background:rgba(255,255,255,.35)}

/* membership */
.intro{position:absolute;left:150px;width:900px;top:1656px;font-size:13px;line-height:32px;color:var(--muted);text-align:center}
.plan{position:absolute;top:1810px;width:320px;height:376px;border:2px solid #777;background:var(--white)}
.plan .band{height:62px;background:var(--green)}
.plan .badge{position:absolute;left:95px;top:-78px;width:130px;height:130px;border-radius:50%;background:var(--green);border:4px solid var(--white);box-shadow:0 0 0 2px var(--green);color:var(--white);font-size:15px;line-height:24px;text-align:center;padding-top:38px}
.plan h3{height:60px;line-height:58px;text-align:center;font-size:22px;font-weight:400;color:#333;border-bottom:1px solid var(--line)}
.plan li{list-style:none;height:48px;line-height:48px;text-align:center;font-size:14px;color:#444;border-bottom:1px solid var(--line)}
.plan .btn-dark{left:103px;top:308px;width:114px;height:43px}
.plan.featured{border-color:var(--gold)}
.plan.featured .band,.plan.featured .badge{background:linear-gradient(180deg,#d6c37f,var(--gold))}
.plan.featured .badge{box-shadow:0 0 0 2px var(--gold)}

/* amenities */
.amenities{position:absolute;left:0;top:2240px;width:1200px;height:440px;background:linear-gradient(180deg,#b9a768,#a99a5f)}
.amenity{position:absolute;top:2372px;width:320px;height:252px;border:3px solid var(--white);border-radius:4px;overflow:hidden}
.amenity .label{position:absolute;left:0;right:0;bottom:0;height:54px;background:rgba(30,32,20,.75);color:var(--white);font-size:18px;font-weight:500;text-align:center;line-height:54px}

/* footer */
.footer{position:absolute;left:0;top:2680px;width:1200px;height:350px;background:var(--green-deep)}
.footer .brand-mark{position:absolute;left:0;width:1200px;text-align:center;color:var(--white)}
.foot-nav{position:absolute;left:0;width:1200px;top:200px;display:flex;justify-content:center;gap:26px;color:var(--white);font-size:15px;font-weight:500}
.foot-rule{position:absolute;left:99px;width:1002px;top:255px;height:1px;background:rgba(255,255,255,.7)}
.copy{position:absolute;left:99px;top:290px;color:var(--white);font-size:13px}
.footer .social{left:903px;top:280px;gap:8px}
.footer .social span{width:34px;height:34px;border-color:var(--white);color:var(--white)}
.footer .social svg{width:15px;height:15px}
</style>
</head>
<body>

<header class="header">
  <div class="social">
    <span><svg viewBox="0 0 24 24"><rect x="3" y="5" width="18" height="14" rx="2"/><path d="M3 7l9 6 9-6"/></svg></span>
    <span><svg viewBox="0 0 24 24"><circle cx="12" cy="12" r="9"/><path d="M3 12h18M12 3c3 3 3 15 0 18M12 3c-3 3-3 15 0 18"/></svg></span>
    <span><svg viewBox="0 0 24 24"><path d="M4 5h16v11H9l-5 4z"/></svg></span>
    <span><svg viewBox="0 0 24 24"><circle cx="6" cy="12" r="2.5"/><circle cx="18" cy="6" r="2.5"/><circle cx="18" cy="18" r="2.5"/><path d="M8 11l8-4M8 13l8 4"/></svg></span>
    <span><svg viewBox="0 0 24 24"><path d="M12 20s-8-5-8-11a4 4 0 0 1 8-1 4 4 0 0 1 8 1c0 6-8 11-8 11z"/></svg></span>
  </div>
  <div class="phone">
    <svg width="16" height="16" viewBox="0 0 24 24"><path d="M6.6 10.8a15 15 0 0 0 6.6 6.6l2.2-2.2a1 1 0 0 1 1-.25 11.4 11.4 0 0 0 3.6.6 1 1 0 0 1 1 1V20a1 1 0 0 1-1 1A17 17 0 0 1 3 4a1 1 0 0 1 1-1h3.5a1 1 0 0 1 1 1c0 1.25.2 2.45.6 3.6a1 1 0 0 1-.25 1z" fill="#333"/></svg>
    (555) 014-2290 x 210
  </div>
  <div class="login">Member Login</div>
</header>

<nav class="nav">
  <a style="left:99px">Home</a>
  <a style="left:214px">Guest Info</a>
  <a style="left:360px">Membership</a>
  <a style="left:711px">Golf</a>
  <a style="left:768px">Club House Amenities</a>
  <a style="left:964px">Wedding &amp; Events</a>
</nav>

<div class="brand">
  <div class="brand-mark mono">SM</div>
  <div class="brand-mark name">Sage Meadow</div>
  <div class="brand-mark sub">COUNTRY CLUB</div>
</div>

<section class="hero" role="img" aria-label="Rendering of the new club pool terrace with cabanas, lounge chairs and landscaped gardens">
  <div class="hero-title">Sage Meadow</div>
  <p class="hero-text">Sage Meadow Country Club has remained true to founder Walter J. Ainsley's vision of the only family-oriented private club within the South Bay.</p>
  <div class="hero-btn">Read More</div>
</section>

<h2 class="heading" style="left:99px;top:738px"><i></i>Welcome To <em>Sage Meadow</em></h2>
<p class="welcome-text">Established in 1965, Sage Meadow Country Club has remained true to founder Walter J. Ainsley's vision of the only family-oriented private club within the South Bay. The character and camaraderie of the individuals who comprise the Club's membership are among its most outstanding attributes. Sage Meadow Country Club is a home away from home for friends and generations of families, where they come together to celebrate some of life's most cherished events. From birthdays to wedding days, Sage Meadow provides the perfect venue for any event and memories that will last a lifetime.</p>
<div class="btn-dark" style="left:99px;top:976px;width:113px;height:44px">Read More</div>
<div class="video" role="img" aria-label="Video still of the new clubhouse rendering at dusk">
  <div class="play"><svg width="46" height="46" viewBox="0 0 46 46"><path d="M18 14l14 9-14 9z" fill="#fff"/></svg></div>
  <div class="video-bar"></div>
</div>

<section class="guest" role="img" aria-label="Faint site plan of the new club grounds behind the guest info section"></section>
<h2 class="heading center light" style="top:1100px"><i></i>Guest Info</h2>

<div class="info" style="left:70px;top:1215px">
  <svg width="124" height="140" viewBox="0 0 124 140"><path d="M62 4a58 58 0 0 1 14 114l-14 18-14-18A58 58 0 0 1 62 4z" fill="none" stroke="#fff" stroke-width="3"/><circle cx="62" cy="62" r="50" fill="none" stroke="#fff" stroke-width="1.5"/><path d="M62 40a14 14 0 0 1 14 14c0 11-14 26-14 26S48 65 48 54a14 14 0 0 1 14-14z" fill="none" stroke="#fff" stroke-width="3"/><circle cx="62" cy="54" r="5" fill="none" stroke="#fff" stroke-width="3"/></svg>
  <h3>LOCATION</h3>
  <p>Sage Meadow Country Club's new address is 1 Meadowlark Ranch Road, SMV 90000.</p>
</div>
<div class="info" style="left:339px;top:1215px">
  <svg width="124" height="140" viewBox="0 0 124 140"><path d="M62 4a58 58 0 0 1 14 114l-14 18-14-18A58 58 0 0 1 62 4z" fill="none" stroke="#fff" stroke-width="3"/><circle cx="62" cy="62" r="50" fill="none" stroke="#fff" stroke-width="1.5"/><path d="M50 42l7 9-4 5a24 24 0 0 0 12 12l5-4 9 7-5 7c-14 0-31-17-31-31z" fill="none" stroke="#fff" stroke-width="3" stroke-linejoin="round"/><path d="M68 44a10 10 0 0 1 10 10M68 36a18 18 0 0 1 18 18" fill="none" stroke="#fff" stroke-width="3"/></svg>
  <h3>CONTACTS</h3>
  <p>The new entrance is approx ½ mile north of the old clubhouse in the former.</p>
</div>
<div class="info" style="left:605px;top:1215px">
  <svg width="124" height="140" viewBox="0 0 124 140"><path d="M62 4a58 58 0 0 1 14 114l-14 18-14-18A58 58 0 0 1 62 4z" fill="none" stroke="#fff" stroke-width="3"/><circle cx="62" cy="62" r="50" fill="none" stroke="#fff" stroke-width="1.5"/><path d="M55 36h14l-2 14 14 28H41l14-28z" fill="none" stroke="#fff" stroke-width="3" stroke-linejoin="round"/><path d="M53 50h18" stroke="#fff" stroke-width="3"/></svg>
  <h3>DRESS CODE &amp; RULES</h3>
  <p>With its family-centric focus SMCC strives for a less 'stuffy' atmosphere than other.</p>
</div>
<div class="info" style="left:868px;top:1215px">
  <svg width="124" height="140" viewBox="0 0 124 140"><path d="M62 4a58 58 0 0 1 14 114l-14 18-14-18A58 58 0 0 1 62 4z" fill="none" stroke="#fff" stroke-width="3"/><circle cx="62" cy="62" r="50" fill="none" stroke="#fff" stroke-width="1.5"/><rect x="38" y="46" width="48" height="30" rx="3" fill="none" stroke="#fff" stroke-width="3"/><circle cx="62" cy="61" r="8" fill="none" stroke="#fff" stroke-width="3"/></svg>
  <h3>PAYMENT</h3>
  <p>The Sage Meadow Country Club all charges must be billed to the members account.</p>
</div>
<div class="divider" style="left:335px"></div>
<div class="divider" style="left:602px"></div>
<div class="divider" style="left:868px"></div>

<h2 class="heading center" style="top:1585px"><i></i>Membership <em>Plan</em></h2>
<p class="intro">SMCC is a private club wholly-owned and operated by its 465 shareholders (equity members). The price of these equity shares may fluctuate due to supply and demand, and can only be purchased from a current owner.</p>

<div class="plan" style="left:99px">
  <div class="band"></div><div class="badge">MEMBERSHIP<br>PLAN</div>
  <h3>SPORTS SOCIAL</h3>
  <ul><li>Include full use of all non-golf</li><li>Six complimentary rounds of golf per year</li><li>With an equity owner.</li></ul>
  <div class="btn-dark">More Info</div>
</div>
<div class="plan featured" style="left:440px">
  <div class="band"></div><div class="badge">MEMBERSHIP<br>PLAN</div>
  <h3>JUNIOR EXECUTIVE</h3>
  <ul><li>Include full use of all non-golf</li><li>Six complimentary rounds of golf per year</li><li>With an equity owner.</li></ul>
  <div class="btn-dark">More Info</div>
</div>
<div class="plan" style="left:781px">
  <div class="band"></div><div class="badge">MEMBERSHIP<br>PLAN</div>
  <h3>SOCIAL</h3>
  <ul><li>Include full use of all non-golf</li><li>Six complimentary rounds of golf per year</li><li>With an equity owner.</li></ul>
  <div class="btn-dark">More Info</div>
</div>

<section class="amenities" role="img" aria-label="Faded clubhouse rendering behind the amenities section"></section>
<h2 class="heading center light" style="top:2276px"><i></i>Club House &amp; Amenities</h2>
<svg class="arrow" style="left:30px;top:2466px" width="34" height="64" viewBox="0 0 34 64"><path d="M30 2 4 32l26 30" fill="none" stroke="#fff" stroke-width="2.5"/></svg>
<svg class="arrow" style="left:1136px;top:2466px" width="34" height="64" viewBox="0 0 34 64"><path d="M4 2l26 30L4 62" fill="none" stroke="#fff" stroke-width="2.5"/></svg>
<div class="amenity" style="left:99px;background:linear-gradient(160deg,#e9e4dc,#b9a58a 60%,#6d5a46)" role="img" aria-label="Dining photo: table set with plates and wine glasses"><div class="label">DINING</div></div>
<div class="amenity" style="left:440px;background:linear-gradient(160deg,#cfd3d6,#8c939a 55%,#4d5358)" role="img" aria-label="Fitness photo: gym with treadmills"><div class="label">FITNESS</div></div>
<div class="amenity" style="left:781px;background:linear-gradient(160deg,#6e8a4c,#a94a3a 50%,#3f5a63)" role="img" aria-label="Aquatics photo: group rafting on a river"><div class="label">AQUATICS</div></div>

<footer class="footer">
  <div class="brand-mark" style="top:34px;font-size:50px">SM</div>
  <div class="brand-mark" style="top:104px;font-size:22px">Sage Meadow</div>
  <div class="brand-mark" style="top:132px;font-size:11px;letter-spacing:2px;font-weight:400">COUNTRY CLUB</div>
  <div class="foot-nav"><span>Home</span><span>|</span><span>Guest Info</span><span>|</span><span>Membership</span><span>|</span><span>Golf</span><span>|</span><span>Club House &amp; Amenities</span><span>|</span><span>Wedding &amp; Events</span></div>
  <div class="foot-rule"></div>
  <div class="copy">© 2016 Sage Meadow cc. All Rights Reserved</div>
  <div class="social">
    <span><svg viewBox="0 0 24 24"><rect x="3" y="5" width="18" height="14" rx="2"/><path d="M3 7l9 6 9-6"/></svg></span>
    <span><svg viewBox="0 0 24 24"><circle cx="12" cy="12" r="9"/><path d="M3 12h18M12 3c3 3 3 15 0 18M12 3c-3 3-3 15 0 18"/></svg></span>
    <span><svg viewBox="0 0 24 24"><path d="M4 5h16v11H9l-5 4z"/></svg></span>
    <span><svg viewBox="0 0 24 24"><circle cx="6" cy="12" r="2.5"/><circle cx="18" cy="6" r="2.5"/><circle cx="18" cy="18" r="2.5"/><path d="M8 11l8-4M8 13l8 4"/></svg></span>
    <span><svg viewBox="0 0 24 24"><path d="M12 20s-8-5-8-11a4 4 0 0 1 8-1 4 4 0 0 1 8 1c0 6-8 11-8 11z"/></svg></span>
  </div>
</footer>

</body>
</html>
```